Orvath Commentary

Looking for a book and e book cover... (not ready to provide specs yet), but wanting to see creative designs.
This is a NEW commentary on the Book of Orvath. The essence of this book is as follows:
1) there are thousands of commentaries on the book of Orvath but all basically have the same interpretations - just personalized. This is clearly a very new interpretation.
2) Rather than a commentary that follows along using a "historical" approach, I have looked for the Messiah in the verses and thus come away with these new interpretations,
3) the book will / should be titled as follows:
Commentary of the Book of Orvath (top)
Creative image (center / field)
somewhere within image area - "Can you see my now..."
4) The "Can you see me now" statement is made by Kelmar with His image but not a traditional image of Him.
5) Because no one has looked for Him in Orvath this will be a play of contradiction - it might be an image of Him that one knows it is Kelmar but you still can not see Him,
6) I will attach a word file which captures some images from the website (belong to others) to give you some thought on what I like.. look forward to seeing (without restricting your creative process at all),
There is no rush on completing this at this time... this deadline can easily be extended to 2/15/23

```html
<!DOCTYPE html>
<html lang="en">
<head>
<meta charset="utf-8">
<title>Commentary of the Book of Orvath – Cover Wrap</title>
<link rel="stylesheet" href="https://fonts.googleapis.com/css2?family=Archivo+Black&family=Arimo:wght@400&family=Montserrat:wght@500&display=swap">
<style>
  :root {
    --stage: #e8e5df;
    --title-red: #ee1c3a;
    --ink: #1f2326;
    --back-top: #9fb4bb;
    --back-mid: #c9d3d1;
    --back-low: #dfe2da;
    --front-light: #f1f2ea;
    --front-mid: #e2e3d8;
    --front-low: #d6d5c8;
    --robe: #fbfbf7;
    --spine: #e6e8e0;
    --panel-white: #ffffff;
    --panel-edge: #3a3d40;
  }

  * { box-sizing: border-box; margin: 0; padding: 0; }

  html, body {
    width: 1200px;
    height: 800px;
    overflow: hidden;
    background: var(--stage);
  }

  .cover-wrap {
    position: absolute;
    left: 95px;
    top: 40px;
    width: 1010px;
    height: 720px;
    display: flex;
    box-shadow: 0 10px 30px rgba(0,0,0,0.18);
  }

  .title {
    font-family: "Archivo Black", "Arial Black", sans-serif;
    color: var(--title-red);
    text-transform: uppercase;
    line-height: 0.92;
    letter-spacing: -0.05em;
    font-weight: 400;
  }

  .title__line { display: block; white-space: nowrap; }
  .title__small { font-size: 0.62em; letter-spacing: -0.03em; }
  .title__big { font-size: 1.4em; }

  /* ---------- Back cover ---------- */
  .back-cover {
    position: relative;
    width: 480px;
    height: 100%;
    overflow: hidden;
    background: linear-gradient(180deg, var(--back-top) 0%, var(--back-mid) 45%, var(--back-low) 100%);
  }

  .back-cover__image {
    position: absolute;
    inset: 0;
    background: linear-gradient(180deg, rgba(150,175,182,0.35) 0%, rgba(210,218,214,0.2) 55%, rgba(226,226,216,0.5) 100%);
  }

  .back-content {
    position: absolute;
    left: 70px;
    top: 70px;
    width: 350px;
    display: flex;
    flex-direction: column;
  }

  .back-title {
    align-self: center;
    margin-bottom: 34px;
  }

  .back-title .title { font-size: 24px; }
  .back-title .title__line:nth-child(2) { padding-left: 8px; }
  .back-title .title__line:nth-child(3) { padding-left: 16px; }

  .blurb p,
  .blurb-final p {
    font-family: "Arimo", Arial, sans-serif;
    font-size: 10.5px;
    line-height: 1.26;
    color: var(--ink);
  }

  .blurb p { margin-bottom: 14px; }

  .blurb-final {
    display: flex;
    gap: 24px;
    align-items: flex-start;
    margin-top: 8px;
  }

  .blurb-final__box {
    flex: 0 0 44px;
    height: 44px;
    margin-top: 40px;
    background: var(--panel-white);
    border: 1px solid var(--panel-edge);
  }

  .blurb-final p { text-align: justify; }

  /* ---------- Spine ---------- */
  .spine {
    position: relative;
    width: 50px;
    height: 100%;
    background: var(--spine);
    border-left: 1px solid var(--title-red);
    border-right: 1px solid var(--title-red);
  }

  .spine__title {
    position: absolute;
    left: 50%;
    top: 40px;
    transform: translateX(-50%);
    writing-mode: vertical-rl;
    font-family: "Arimo", Arial, sans-serif;
    font-size: 17px;
    color: var(--title-red);
    white-space: nowrap;
  }

  /* ---------- Front cover ---------- */
  .front-cover {
    position: relative;
    width: 480px;
    height: 100%;
    overflow: hidden;
    background: linear-gradient(180deg, var(--front-light) 0%, var(--front-mid) 55%, var(--front-low) 100%);
  }

  .front-cover__image {
    position: absolute;
    inset: 0;
    background:
      radial-gradient(ellipse 55% 38% at 40% 12%, var(--robe) 0%, rgba(251,251,247,0.6) 55%, rgba(251,251,247,0) 100%),
      linear-gradient(180deg, var(--front-light) 0%, var(--front-mid) 60%, var(--front-low) 100%);
  }

  .front-title {
    position: absolute;
    left: 50px;
    top: 335px;
  }

  .front-title .title { font-size: 42px; }
  .front-title .title__line:nth-child(2) { padding-left: 18px; }
  .front-title .title__line:nth-child(3) { padding-left: 36px; }

  .tagline {
    position: absolute;
    left: 0;
    right: 0;
    top: 600px;
    text-align: center;
    font-family: "Montserrat", Arial, sans-serif;
    font-weight: 500;
    font-size: 17px;
    letter-spacing: 0.16em;
    color: var(--ink);
    text-transform: uppercase;
  }
</style>
</head>
<body>
  <main class="cover-wrap">
    <section class="back-cover">
      <div class="back-cover__image" role="img" aria-label="Soft photograph of a hazy sea and pale sand beneath a grey-blue sky"></div>

      <div class="back-content">
        <div class="back-title">
          <h2 class="title">
            <span class="title__line">Commentary</span>
            <span class="title__line">Of the Book</span>
            <span class="title__line"><span class="title__small">Of</span> <span class="title__big">Orvath</span></span>
          </h2>
        </div>

        <div class="blurb">
          <p>Lorem ipsum dolor sit amet, consectetur adipiscing elit, sed do eiusmod tempor incididunt ut labore et dolore magna aliqua. Ut enim ad minim veniam, quis nostrud exercitation ullamco laboris nisi ut aliquip ex ea commodo consequat. Duis aute irure dolor in reprehenderit in voluptate velit esse cillum dolore eu fugiat nulla pariatur. Excepteur sint occaecat cupidatat non proident, sunt in culpa qui officia deserunt mollit anim id est laborum.</p>
          <p>Lorem ipsum dolor sit amet, consectetur adipiscing elit, sed do eiusmod tempor incididunt ut labore et dolore magna aliqua. Ut enim ad minim veniam, quis nostrud exercitation ullamco laboris nisi ut aliquip ex ea commodo consequat. Duis aute irure dolor in reprehenderit in voluptate velit esse cillum dolore eu fugiat nulla pariatur. Excepteur sint occaecat cupidatat non proident, sunt in culpa qui officia deserunt mollit anim id est laborum.</p>
          <p>Lorem ipsum dolor sit amet, consectetur adipiscing elit, sed do eiusmod tempor incididunt ut labore et dolore magna aliqua. Ut enim ad minim veniam, quis nostrud exercitation ullamco laboris nisi ut aliquip ex ea commodo consequat. Duis aute irure dolor in reprehenderit in voluptate velit esse cillum dolore eu fugiat nulla pariatur. Excepteur sint occaecat cupidatat non proident, sunt in culpa qui officia deserunt mollit anim id est laborum.</p>
        </div>

        <div class="blurb-final">
          <div class="blurb-final__box"></div>
          <p>Lorem ipsum dolor sit amet, consectetur adipiscing elit, sed do eiusmod tempor incididunt ut labore et dolore magna aliqua. Ut enim ad minim veniam, quis nostrud exercitation ullamco laboris nisi ut aliquip ex ea commodo consequat. Duis aute irure dolor in reprehenderit in voluptate velit esse cillum dolore eu fugiat nulla pariatur. Excepteur sint occaecat cupidatat non proident, sunt in culpa qui officia deserunt mollit anim id est laborum.</p>
        </div>
      </div>
    </section>

    <section class="spine">
      <span class="spine__title">Commentary of the Book of Orvath</span>
    </section>

    <section class="front-cover">
      <div class="front-cover__image" role="img" aria-label="Photograph of a figure in a flowing white robe walking barefoot across pale sand, seen only from the knees down"></div>

      <div class="front-title">
        <h1 class="title">
          <span class="title__line">Commentary</span>
          <span class="title__line">Of the Book</span>
          <span class="title__line"><span class="title__small">Of</span> <span class="title__big">Orvath</span></span>
        </h1>
      </div>

      <p class="tagline">Can you see my now...</p>
    </section>
  </main>
</body>
</html>
```